Real Estate Agency Chatterlane Cover Photo

We need a Chatterlane cover photo created for our Real Estate Business. We also need this cover photo adapted to several other platforms. Please read this brindlo doc for full specifications of the job https://files.brindlo-example.net/sheet/d/8QwerPLm4ZxVb2NnKs7RtYhUe3_gHdjAoFcWsMvBn/view?mode=share

Please also carefully read the Must Haves/Should Not Haves

Please contact me if you have any queries. Looking forward to seeing your designs!

Owen

Industry/Entity Type

Real Estate Agent

Requirements
Must have
• The Taglines 'More Money In Your Pocket' and sub tagline 'With Our Low Flat Fee To Sell Your Home'

It can then also have other elements e.g our logo, contact details and anything else you think will work well.

It must also have great graphic design work which looks custom and very clean/modern
Should not have
• Must not have poor quality stock images or anything tacky regarding money etc

```html
<!DOCTYPE html>
<html lang="en">
<head>
<meta charset="utf-8">
<title>Fairmark Cover</title>
<link rel="stylesheet" href="https://fonts.googleapis.com/css2?family=Nunito+Sans:wght@300;400;700;800&display=swap">
<style>
  :root {
    --page-bg: #ffffff;
    --photo-sky: #62666b;
    --photo-mid: #4a4d50;
    --photo-grass: #4a5338;
    --photo-ground: #3c3b33;
    --overlay: rgba(20, 22, 26, 0.28);
    --brand-red: #e0242b;
    --text-light: #ffffff;
  }
  * { margin: 0; padding: 0; box-sizing: border-box; }
  html, body {
    width: 1200px;
    height: 781px;
    overflow: hidden;
    background: var(--page-bg);
  }
  .canvas {
    position: relative;
    width: 1200px;
    height: 781px;
    background: var(--page-bg);
  }
  .cover {
    position: absolute;
    left: 74px;
    top: 110px;
    width: 1050px;
    height: 588px;
    overflow: hidden;
    font-family: "Nunito Sans", "Helvetica Neue", Arial, sans-serif;
  }
  .cover-photo {
    position: absolute;
    inset: 0;
    background:
      radial-gradient(ellipse 60% 35% at 75% 30%, rgba(40, 36, 32, 0.55), transparent 70%),
      linear-gradient(180deg,
        var(--photo-sky) 0%,
        var(--photo-mid) 45%,
        var(--photo-grass) 62%,
        var(--photo-grass) 80%,
        var(--photo-ground) 100%);
  }
  .cover-overlay {
    position: absolute;
    inset: 0;
    background: var(--overlay);
  }
  .brand-name {
    position: absolute;
    left: 65px;
    top: 44px;
    font-size: 48px;
    font-weight: 700;
    letter-spacing: 3px;
    line-height: 1;
    color: var(--brand-red);
    text-transform: uppercase;
  }
  .tagline {
    position: absolute;
    left: 0;
    right: 0;
    top: 228px;
    text-align: center;
    color: var(--text-light);
  }
  .tagline-main {
    font-size: 60px;
    font-weight: 800;
    line-height: 1.1;
    letter-spacing: 0.2px;
  }
  .tagline-sub {
    margin-top: 2px;
    font-size: 35px;
    font-weight: 300;
    line-height: 1.2;
  }
</style>
</head>
<body>
  <div class="canvas">
    <section class="cover">
      <div class="cover-photo" role="img" aria-label="Photograph of a group of people standing on a grassy roadside verge under bare autumn trees"></div>
      <div class="cover-overlay"></div>
      <div class="brand-name">Fairmark</div>
      <div class="tagline">
        <h1 class="tagline-main">More Money In Your Pocket</h1>
        <p class="tagline-sub">With our Low Flat Fee To Sell Your Home</p>
      </div>
    </section>
  </div>
</body>
</html>
```